Industrial Automation company requires a business card design

Valtrin Automation provides design & build of Automated Equipment for manufacturing industry.
www.valtrinautomation.example
The equipment we design is used for manufacturing in sectors such as medical device, pharmaceutical, aerospace and electronics.
We require a new business card design which incorporates our (New) logo and the key message words:
Automated Equipment:
Design, Build, Control, Test, Support

```html
<!DOCTYPE html>
<html lang="en">
<head>
<meta charset="utf-8">
<title>Valtrin Automation – Business Card</title>
<link href="https://fonts.googleapis.com/css2?family=Arimo:wght@400;700&display=swap" rel="stylesheet">
<style>
  :root {
    --brand-green: #1f8a3c;
    --ink: #111111;
    --text: #2b2b2b;
    --paper: #ffffff;
  }
  html, body {
    margin: 0;
    padding: 0;
    overflow: hidden;
    background: var(--paper);
  }
  .card {
    position: relative;
    width: 1200px;
    height: 686px;
    background: var(--paper);
    font-family: "Arimo", Arial, sans-serif;
    overflow: hidden;
  }
  .brand {
    position: absolute;
    left: 50px;
    top: 42px;
    display: flex;
    align-items: center;
    gap: 22px;
    color: var(--brand-green);
  }
  .brand-dot {
    width: 82px;
    height: 82px;
    border-radius: 50%;
    background: var(--brand-green);
    flex: none;
  }
  .brand-name {
    font-weight: 700;
    font-size: 50px;
    line-height: 1;
    letter-spacing: 1px;
  }
  .key-message {
    position: absolute;
    left: 54px;
    top: 414px;
    width: 500px;
    margin: 0;
    font-size: 30px;
    line-height: 56px;
    color: var(--text);
  }
  .key-message-title {
    display: block;
    font-weight: 700;
    color: var(--brand-green);
  }
  .key-message-services {
    display: block;
  }
  .contact {
    position: absolute;
    left: 614px;
    top: 258px;
    width: 579px;
  }
  .person-name {
    margin: 0;
    font-size: 54px;
    font-weight: 700;
    line-height: 1;
    color: var(--ink);
  }
  .person-role {
    margin: 14px 0 0;
    font-size: 34px;
    font-weight: 700;
    line-height: 1;
    color: var(--ink);
  }
  .divider {
    height: 4px;
    background: var(--ink);
    margin: 20px 0 0;
    border: 0;
  }
  .details {
    list-style: none;
    margin: 24px 0 0;
    padding: 0;
    font-size: 34px;
    line-height: 55px;
    color: var(--text);
  }
  .details .label {
    font-weight: 700;
    color: var(--ink);
  }
</style>
</head>
<body>
  <div class="card">
    <div class="brand">
      <span class="brand-dot" aria-hidden="true"></span>
      <span class="brand-name">Valtrin Automation</span>
    </div>

    <p class="key-message">
      <span class="key-message-title">Automated Equipment:</span>
      <span class="key-message-services">Design, Build, Control,</span>
      <span class="key-message-services">Test, Support</span>
    </p>

    <div class="contact">
      <h1 class="person-name">John Doe</h1>
      <p class="person-role">Manager</p>
      <hr class="divider">
      <ul class="details">
        <li class="address">Glenmorra, Co. Kerrow, Ireland</li>
        <li class="website">www.valtrinautomation.example</li>
        <li class="phone"><span class="label">Phone:</span> 00 353 (0) 41 58 2290</li>
        <li class="fax"><span class="label">Fax:</span> 00 353 (0) 41 58 2291</li>
      </ul>
    </div>
  </div>
</body>
</html>
```